Plastic Surgeon Stationary Design

I Already have the logo. I Want and a clean, minimalist and elegant project. Please, I prefer Black, White and Gold color but you're free to try another ones. Business card,
Letterhead (A4 and Office), Recipes (Letter Pad) (A5), Envelop, Invoice, Computer Bill, Bill Book, Single A4 page size,
You Have to create at least the same materials I already own. I would like to a file to use in word to print letterheads and letter pad.
What I want that you make more changes are the envelopes that are to colorful and not elegant.
I'll not accept any design without my addresses as you can guide yourself with the models I provide.
Here are the addresses too:
"www.rubemtavorasilva.example" (website)
(My clinics' address)
"SÃO PAULO
Rua Lucas Bentim, 3180, Lucas Bentim Office, Cj 204
São Paulo - SP
(11) 90123-4567"
"BALNEÁRIO CAMBORIÚ
Rua Clemente Vilaça, 418, 7° andar
Edificio Torre Quaresma
Balneário Camboriú - SC
(047) 9012-3456"
Attention: Letterheads, Recipes, have to contain "CRM/SC 52.807 and CRM/SP 308.614" close to my name (Dr. Rubem Távora - Cirurgião Plástico), it is usually placed at the bottom.
Designers, attention!
During the process of creating bear in mind that the details of the logo, as the faces on the sides, are designed to be subtle. Highlight other such details affect the delicacy and elegance of the logo and visual identity.
When you are creating stationery, do not abuse the use of the logo, it should be used once or at most two times in each item.
Remember! Each stationery set must submit 3 models, one with the address "Balneario Camboriu", another with the address of "São Paulo" and the third containing both addresses.
The model letter envelope, folder type bag for letterhead and folder with inner pocket that provided a model did not please me because they are very flashy. Give preference to the use of white or black background.
PLEASE! Seek inspiration in the models contained in this link:
https://www.filecrate.example/sh/kq27zp41wcx905m/PlRtVuY_QX
In this link you can find my PAST Stationary Itens, so it can help you on your work
https://docuvault.example/7ZK3NB8QeT2LwYhR
Reason: Nobody presented anything useful.
Reason: still waiting some designers send their projects
Reason: Still Waiting Some Designs....
Target Market(s)
Mostly females with good economical condition. (Class A and AB)
Industry/Entity Type
Business
Requirements
Must have
- You have to provide 3 models of each paper, one with the address of São Paulo, another with the Balneario Camboriú address, and the third one with both addresses.

```html
<!DOCTYPE html>
<html lang="pt-BR">
<head>
<meta charset="utf-8">
<title>Rubem Távora – Papelaria</title>
<link rel="stylesheet" href="https://fonts.googleapis.com/css2?family=Exo+2:wght@400;500;600&display=swap">
<style>
  :root {
    --backdrop: #efefef;
    --paper: #f7f7f7;
    --ink: #3a3a3a;
    --band: #2b2b2b;
    --black: #1c1c1c;
    --gold: #e3b22a;
    --pin: #e08a5a;
    --ghost: #e4e4e4;
  }
  * { margin: 0; padding: 0; box-sizing: border-box; }
  html, body { width: 1200px; height: 1000px; overflow: hidden; }
  body {
    position: relative;
    background: var(--backdrop);
    font-family: "Exo 2", sans-serif;
    color: var(--ink);
  }
  .item { position: absolute; }
  .brand-name {
    font-family: "Exo 2", sans-serif;
    font-weight: 500;
    white-space: nowrap;
  }

  /* Contact list */
  .contact-list { list-style: none; font-size: 5.2px; line-height: 6.4px; }
  .contact-list li { display: flex; align-items: flex-start; gap: 3px; white-space: nowrap; }
  .contact-icon { width: 5px; height: 5px; flex: none; margin-top: 0.7px; }

  /* Letterhead */
  .letterhead { left: 212px; top: 124px; width: 341px; height: 522px; background: var(--paper); overflow: hidden; }
  .letterhead-band { height: 80px; background: var(--band); display: flex; align-items: center; justify-content: center; }
  .letterhead-band .brand-name { color: #fff; font-size: 19px; }
  .letter-mark { position: absolute; left: 110px; top: 320px; width: 165px; height: 162px; border-radius: 50%; background: var(--ghost); }
  .letter-body { position: absolute; left: 61px; top: 138px; width: 251px; font-size: 6.3px; line-height: 7.6px; text-align: justify; color: #444; }
  .letter-body p { margin-bottom: 7.6px; }
  .signature { position: absolute; left: 180px; top: 372px; width: 128px; height: 16px; background: #d6d6d6; border-radius: 3px; }
  .letter-crm { position: absolute; left: 50px; top: 490px; font-size: 5.2px; line-height: 6.4px; color: #555; }
  .letterhead .contact-list { position: absolute; left: 241px; top: 472px; color: #555; }
  .letterhead .contact-icon { fill: var(--pin); stroke: var(--pin); }

  /* Folder */
  .folder { left: 646px; top: 100px; width: 436px; height: 550px; background: var(--black); }
  .folder::before { content: ""; position: absolute; left: 4px; top: 0; bottom: 0; width: 10px; border-left: 1px solid #2c2c2c; border-right: 1px solid #2c2c2c; }
  .folder .brand-name { position: absolute; left: 85px; top: 150px; color: var(--gold); font-size: 26px; }

  /* Business cards */
  .card { left: 80px; width: 166px; height: 95px; background: var(--black); }
  .card-front { top: 692px; display: flex; align-items: center; justify-content: center; }
  .card-front .brand-name { color: var(--gold); font-size: 11px; }
  .card-back { top: 812px; color: #ddd; text-align: center; }
  .card-back .dot-mark { width: 6px; height: 6px; border-radius: 50%; background: var(--gold); margin: 8px auto 3px; }
  .card-name { font-size: 8px; font-weight: 500; color: #fff; }
  .card-role { font-size: 5.2px; font-style: italic; line-height: 7px; }
  .card-foot { position: absolute; left: 5px; right: 5px; bottom: 5px; display: flex; justify-content: space-between; text-align: left; font-size: 3.4px; line-height: 4.3px; color: #bbb; }
  .card-foot .web { align-self: flex-start; }

  /* Envelopes */
  .envelope { top: 706px; height: 197px; background: var(--black); }
  .envelope-front { left: 290px; width: 412px; }
  .envelope-front .brand-name { position: absolute; left: 18px; top: 152px; color: var(--gold); font-size: 15px; }
  .envelope-back { left: 742px; width: 414px; }
  .envelope-flap { position: absolute; left: 0; top: 0; }
  .envelope-back .brand-name { position: absolute; left: 295px; top: 131px; color: var(--gold); font-size: 8.5px; }
  .envelope-back .contact-list { position: absolute; left: 285px; top: 150px; color: #ccc; }
  .envelope-back .contact-icon { fill: var(--gold); stroke: var(--gold); }
</style>
</head>
<body>

<section class="item letterhead">
  <header class="letterhead-band"><span class="brand-name">Rubem Távora</span></header>
  <div class="letter-mark" role="img" aria-label="Faint brand emblem in the background"></div>
  <div class="letter-body">
    <p>Dear Client</p>
    <p>Lorem ipsum dolor sit amet, consectetur adipiscing elit. Nulla sodales nisi vitae Lorem ipsum dolor sit amet, consectetur adipiscing elit. Suspendisse feugiat eros nisl, a facilisis risus eleifend sed. Aliquam mauris enim, fermentum eu lacinia sit amet, laoreet eu leo. Nullam eleifend nulla in libero tristique, ac vulputate odio tincidunt. Etiam non condimentum tortor. Integer suscipit neque nec odio porttitor cursus. Phasellus a sapien blandit, suscipit justo id, condimentum ante. Morbi tristique justo risus, id mattis dui molestie ut. Nullam volutpat ut quam commodo faucibus. Pellentesque urna est, interdum in elit quis, pharetra elementum orci. Nam pharetra velit molestie justo placerat scelerisque.</p>
    <p>ullam aliquam ligula ac sem aliquet varius. Nullam sed laoreet sapien. Fusce ultricies lobortis odio, sed imperdiet magna lacinia egestas. Morbi vitae varius nibh. Phasellus purus felis, congue id tempor quis, porttitor ut sem. Integer turpis nunc, posuere at quam interdum, interdum pharetra lectus. Fusce commodo sapien vel consequat tincidunt. Proin sed nisl dignissim, accumsan dui ut, luctus turpis. Praesent vulputate elementum nibh. Ut volutpat felis ut mi tincidunt, vitae accumsan quam porta. Sed malesuada bibendum lectus tempor ullamcorper. Nullam interdum diam velit, id porta elit congue quis.</p>
    <p>Best regards.</p>
  </div>
  <div class="signature" role="img" aria-label="Handwritten signature of Dr. Rubem Távora"></div>
  <div class="letter-crm">CRM/SC 52.807<br>CRM/SP 308.614</div>
  <ul class="contact-list">
    <li><svg class="contact-icon" viewBox="0 0 10 10"><path d="M5 0a3.5 3.5 0 0 0-3.5 3.5C1.5 6 5 10 5 10s3.5-4 3.5-6.5A3.5 3.5 0 0 0 5 0z" stroke="none"/></svg><span>Rua Lucas Bentim, 3180, Lucas<br>Bentim Office, Cj 204<br>São Paulo - SP</span></li>
    <li><svg class="contact-icon" viewBox="0 0 10 10"><path d="M2 0h2l1 3-1.5 1a6 6 0 0 0 2.5 2.5L7 5l3 1v2c0 1-1 2-2 2A8 8 0 0 1 0 2c0-1 1-2 2-2z" stroke="none"/></svg><span>(11) 90123-4567</span></li>
    <li><svg class="contact-icon" viewBox="0 0 10 10"><circle cx="5" cy="5" r="4" fill="none" stroke-width="1.5"/></svg><span>www.rubemtavorasilva.example</span></li>
  </ul>
</section>

<section class="item folder">
  <span class="brand-name">Rubem Távora</span>
</section>

<section class="item card card-front">
  <span class="brand-name">Rubem Távora</span>
</section>

<section class="item card card-back">
  <div class="dot-mark"></div>
  <div class="card-name">Dr. Rubem Távora</div>
  <div class="card-role">Cirurgião Plástico<br>Membro da Sociedade Nacional de Cirurgia Estética<br>CRM/SC 52.807 · CRM/SP 308.614</div>
  <div class="card-foot">
    <span>BALNEÁRIO CAMBORIÚ<br>Rua Clemente Vilaça, 418, 7° andar<br>Edificio Torre Quaresma<br>Balneário Camboriú - SC<br>(047) 9012-3456</span>
    <span class="web">www.rubemtavorasilva.example</span>
    <span>SÃO PAULO<br>Rua Lucas Bentim, 3180,<br>Lucas Bentim Office, Cj 204<br>São Paulo - SP<br>(11) 90123-4567</span>
  </div>
</section>

<section class="item envelope envelope-front">
  <span class="brand-name">Rubem Távora</span>
</section>

<section class="item envelope envelope-back">
  <svg class="envelope-flap" viewBox="0 0 414 197" width="414" height="197"><path d="M14 0v66q0 4 4 4h378q4 0 4-4V0" fill="none" stroke="#2e2e2e" stroke-width="1"/></svg>
  <span class="brand-name">Rubem Távora</span>
  <ul class="contact-list">
    <li><svg class="contact-icon" viewBox="0 0 10 10"><path d="M5 0a3.5 3.5 0 0 0-3.5 3.5C1.5 6 5 10 5 10s3.5-4 3.5-6.5A3.5 3.5 0 0 0 5 0z" stroke="none"/></svg><span>Rua Lucas Bentim, 3180, Lucas Bentim<br>Office, Cj 204<br>São Paulo - SP</span></li>
    <li><svg class="contact-icon" viewBox="0 0 10 10"><path d="M2 0h2l1 3-1.5 1a6 6 0 0 0 2.5 2.5L7 5l3 1v2c0 1-1 2-2 2A8 8 0 0 1 0 2c0-1 1-2 2-2z" stroke="none"/></svg><span>(11) 90123-4567</span></li>
    <li><svg class="contact-icon" viewBox="0 0 10 10"><circle cx="5" cy="5" r="4" fill="none" stroke-width="1.5"/></svg><span>www.rubemtavorasilva.example</span></li>
  </ul>
</section>

</body>
</html>
```